Profesional personal website needs design and business card

I need a business card with my professional name as a logo "Marlo Vitality" for my business. I am a Wellness Coach, consultant and trainer. So it should be professional, wellness oriented and modern.

Target Market(s)

Private clients, governments, corporations. Luxury and high market.

Industry/Entity Type

Health And Wellness

Contact Information for Business Card

Marlo Vitality should be the logo

Colors

Designer to choose colors to be used in the design.

Requirements
Must have
• Marlo Vitality
• Name: Tomás Arribal
• Wellness Coach, Consultant & Trainer.
• Website: www.marlovitality.example
• Phone:
• Spain (+34) 612 480 397
• (USA) +1 (555) 318 2046
Nice to have
• The most important is the design of "Marlo Vitality", as this is going to be my personal brand logo. It should be professional, wellness, high end and actual.
Should not have
• no golds, no baroque style..

```html
<!DOCTYPE html>
<html lang="en">
<head>
<meta charset="utf-8">
<title>Marlo Vitality – Business Card</title>
<link rel="stylesheet" href="https://fonts.googleapis.com/css2?family=Montserrat:wght@400;500;700&display=swap">
<style>
  :root {
    --backdrop: #161616;
    --card: #262626;
    --card-edge: #2e2e2e;
    --accent: #f5c400;
    --ink: #ffffff;
    --ink-soft: #e6e6e6;
    --emboss: #3a3a3a;
  }
  * { box-sizing: border-box; margin: 0; padding: 0; }
  html, body {
    width: 1200px; height: 900px; overflow: hidden;
    background: var(--backdrop);
    font-family: "Montserrat", sans-serif;
  }
  .sheet {
    position: relative; width: 1200px; height: 900px;
    display: flex; flex-direction: column; align-items: center; justify-content: center; gap: 34px;
  }
  .card {
    position: relative; width: 700px; height: 400px;
    background: linear-gradient(135deg, var(--card) 0%, var(--card-edge) 100%);
    border-bottom: 7px solid var(--accent);
    box-shadow: 0 18px 40px rgba(0,0,0,.55);
    overflow: hidden;
  }
  .brand-name {
    font-weight: 700; line-height: 1; white-space: nowrap; text-transform: uppercase;
  }

  /* front */
  .card--front { display: flex; align-items: center; justify-content: center; }
  .card--front .brand-name { color: var(--emboss); font-size: 44px; letter-spacing: 4px; }

  /* back */
  .card--back { display: flex; align-items: center; padding-left: 56px; }
  .card--back .brand-name { color: var(--ink); font-size: 24px; letter-spacing: 2px; }
  .divider { width: 3px; height: 190px; background: var(--accent); margin: 0 30px; flex: none; }
  .details { color: var(--ink-soft); white-space: nowrap; }
  .person-name { color: var(--accent); font-weight: 700; font-size: 24px; letter-spacing: 1px; }
  .person-role { font-size: 16px; font-weight: 500; line-height: 1.3; margin: 6px 0 16px; }
  .contact-list { list-style: none; font-size: 16px; font-weight: 500; }
  .contact-list li { display: flex; align-items: center; gap: 10px; height: 26px; }
  .contact-list svg { width: 15px; height: 15px; flex: none; }
  .contact-list .flag { width: 24px; height: 15px; margin-left: 14px; }
  .web-domain { color: var(--accent); }
</style>
</head>
<body>
<main class="sheet">
  <section class="card card--front">
    <div class="brand-name">Marlo Vitality</div>
  </section>

  <section class="card card--back">
    <div class="brand-name">Marlo Vitality</div>
    <div class="divider"></div>
    <div class="details">
      <h1 class="person-name">TOMÁS ARRIBAL</h1>
      <p class="person-role">Wellness Coach,<br>Consultant &amp; Trainer</p>
      <ul class="contact-list">
        <li>
          <svg viewBox="0 0 16 16" aria-hidden="true"><path d="M4 1.5l2.2 3-1.3 1.6c.9 2 2.4 3.5 4.4 4.4l1.6-1.3 3 2.2-1.2 2.3C7.5 13.5 2.5 8.5 1.7 3.3z" fill="none" stroke="#f5c400" stroke-width="1.4"/></svg>
          (+34) 612 480 397
          <svg class="flag" viewBox="0 0 24 15" aria-hidden="true"><rect width="24" height="15" fill="#c60b1e"/><rect y="4" width="24" height="7" fill="#ffc400"/></svg>
        </li>
        <li>
          <svg viewBox="0 0 16 16" aria-hidden="true"><rect x="4" y="1" width="8" height="14" rx="1.5" fill="none" stroke="#f5c400" stroke-width="1.4"/><line x1="7" y1="12.5" x2="9" y2="12.5" stroke="#f5c400" stroke-width="1.4"/></svg>
          +1 (555) 318 2046
          <svg class="flag" viewBox="0 0 24 15" aria-hidden="true"><rect width="24" height="15" fill="#ffffff"/><g fill="#b22234"><rect width="24" height="1.5"/><rect y="3" width="24" height="1.5"/><rect y="6" width="24" height="1.5"/><rect y="9" width="24" height="1.5"/><rect y="12" width="24" height="1.5"/></g><rect width="10" height="7.5" fill="#3c3b6e"/></svg>
        </li>
        <li>
          <svg viewBox="0 0 16 16" aria-hidden="true"><rect x="1.5" y="3.5" width="13" height="9" fill="none" stroke="#f5c400" stroke-width="1.4"/><path d="M1.5 3.5l6.5 5 6.5-5" fill="none" stroke="#f5c400" stroke-width="1.4"/></svg>
          info@marlovitality.example
        </li>
        <li>
          <svg viewBox="0 0 16 16" aria-hidden="true"><g fill="none" stroke="#f5c400" stroke-width="1.3"><circle cx="8" cy="8" r="6.5"/><ellipse cx="8" cy="8" rx="3" ry="6.5"/><line x1="1.5" y1="8" x2="14.5" y2="8"/></g></svg>
          <span>www.<span class="web-domain">marlovitality</span>.example</span>
        </li>
      </ul>
    </div>
  </section>
</main>
</body>
</html>
```